Minimalist Modern Business Card Design, open to ideas, or cleaner version of provided files, but what logo & logo colors (with some black) as shown in files, and info for back shown in files as well.

```html
<!DOCTYPE html>
<html lang="en">
<head>
<meta charset="utf-8">
<title>Trailhead Truck Care – Business Card</title>
<link href="https://fonts.googleapis.com/css2?family=Montserrat:wght@400;500;700;800&display=swap" rel="stylesheet">
<style>
  :root {
    --navy: #24245e;
    --ink: #1c1c24;
    --card: #f2f2f4;
    --page: #dcdde0;
    --rule: #1a1a1a;
  }
  * { box-sizing: border-box; margin: 0; padding: 0; }
  html, body { width: 1200px; height: 1200px; overflow: hidden; }
  body {
    background: var(--page);
    font-family: "Montserrat", Arial, sans-serif;
    color: var(--ink);
    position: relative;
  }
  .card {
    position: absolute;
    left: 236px;
    width: 729px;
    height: 416px;
    background: var(--card);
    border-radius: 4px;
    box-shadow: 0 6px 18px rgba(0,0,0,0.18);
    overflow: hidden;
  }
  .card--front { top: 150px; }
  .card--back { top: 630px; }

  /* Front */
  .brand {
    position: absolute;
    left: 420px;
    top: 44px;
    display: flex;
    align-items: center;
    gap: 16px;
  }
  .brand__square { width: 54px; height: 54px; background: var(--navy); }
  .brand__name {
    color: var(--navy);
    font-weight: 700;
    font-size: 34px;
    line-height: 34px;
  }
  .person { position: absolute; left: 56px; top: 200px; }
  .person__name { color: var(--navy); font-weight: 800; font-size: 32px; line-height: 36px; }
  .person__role { font-size: 19px; font-weight: 500; margin-top: 6px; }
  .divider {
    position: absolute;
    left: 56px; right: 56px; top: 275px;
    height: 2px; background: var(--rule);
  }
  .contacts { position: absolute; left: 56px; top: 290px; list-style: none; }
  .contacts li {
    display: flex; align-items: center; gap: 10px;
    font-size: 19px; font-weight: 500; line-height: 27.5px;
  }
  .contacts svg { width: 16px; height: 16px; fill: var(--navy); }
  .address {
    position: absolute; right: 56px; top: 312px;
    text-align: right; font-size: 19px; font-weight: 500; line-height: 28px;
  }

  /* Back */
  .section-title {
    position: absolute; left: 0; right: 0;
    text-align: center; color: var(--navy);
    font-weight: 800; font-size: 19px;
  }
  .section-title--services { top: 30px; }
  .section-title--specialties { top: 197px; }
  .list {
    position: absolute; list-style: none;
    font-size: 19px; line-height: 25.2px; font-weight: 500;
  }
  .list li { display: flex; align-items: center; gap: 14px; white-space: nowrap; }
  .list li::before {
    content: ""; width: 10px; height: 10px;
    background: var(--navy); transform: rotate(45deg); flex: none;
  }
  .list--services-a { left: 34px; top: 62px; }
  .list--services-b { left: 345px; top: 62px; }
  .list--specialties-a { left: 34px; top: 229px; }
  .list--specialties-b { left: 345px; top: 229px; }
  .regions {
    position: absolute; left: 0; right: 0; top: 369px; height: 24px;
    background: var(--navy); color: #e8e8f0;
    font-size: 18px; line-height: 24px;
  }
  .regions span { position: absolute; top: 0; }
</style>
</head>
<body>

<section class="card card--front">
  <div class="brand">
    <div class="brand__square"></div>
    <div class="brand__name">Trailhead<br>Truck Care</div>
  </div>

  <div class="person">
    <h1 class="person__name">Dorian Vale</h1>
    <p class="person__role">Founder &amp; Director</p>
  </div>

  <div class="divider"></div>

  <ul class="contacts">
    <li>
      <svg viewBox="0 0 24 24"><path d="M6.6 10.8a15.1 15.1 0 0 0 6.6 6.6l2.2-2.2c.3-.3.7-.4 1-.2 1.1.4 2.3.6 3.6.6.6 0 1 .4 1 1V20c0 .6-.4 1-1 1A17 17 0 0 1 3 4c0-.6.4-1 1-1h3.5c.6 0 1 .4 1 1 0 1.3.2 2.5.6 3.6.1.3 0 .7-.2 1z"/></svg>
      (555)-014-2297
    </li>
    <li>
      <svg viewBox="0 0 24 24"><path d="M2 5h20v14H2z M4 7v.5l8 5 8-5V7l-8 5z" fill-rule="evenodd"/></svg>
      info@truckcareco.com
    </li>
    <li>
      <svg viewBox="0 0 24 24"><path d="M12 2a10 10 0 1 0 0 20 10 10 0 0 0 0-20zm-1 2.1V11H7.1c.2-3 1.7-5.6 3.9-6.9zm2 0c2.2 1.3 3.7 3.9 3.9 6.9H13zM4.1 11h1c.1-2 .7-3.9 1.7-5.3A8 8 0 0 0 4.1 11zm13.8 0h1a8 8 0 0 0-2.7-5.3 10.6 10.6 0 0 1 1.7 5.3zM4.1 13a8 8 0 0 0 2.7 5.3A10.6 10.6 0 0 1 5.1 13zm3 0H11v6.9c-2.2-1.3-3.7-3.9-3.9-6.9zM13 13h3.9c-.2 3-1.7 5.6-3.9 6.9zm5.9 0a10.6 10.6 0 0 1-1.7 5.3 8 8 0 0 0 2.7-5.3z"/></svg>
      www.truckcareco.com
    </li>
  </ul>

  <address class="address" style="font-style: normal;">
    4180 Alder Road<br>
    Pine Hollow Oregon 97001
  </address>
</section>

<section class="card card--back">
  <h2 class="section-title section-title--services">SERVICES INCLUDE:</h2>
  <ul class="list list--services-a">
    <li>Shop &amp; Mobile</li>
    <li>DoT &amp; BIT Inspections</li>
    <li>All Maintenance &amp; Repairs</li>
    <li>Check Engine Lights</li>
    <li>Dealer Certified Techs</li>
  </ul>
  <ul class="list list--services-b">
    <li>Diags, regens &amp; Programming</li>
    <li>Full Dealer Software Capabilities</li>
    <li>PM &amp; Compliance Tracking</li>
    <li>App-Based Billing &amp; Live Updates</li>
    <li>Night Servicing to Avoid Downtime</li>
  </ul>

  <h2 class="section-title section-title--specialties">SPECIALIZING IN:</h2>
  <ul class="list list--specialties-a">
    <li>Heavy &amp; Medium Duty</li>
    <li>After Treatment</li>
    <li>Freightmark</li>
    <li>Kenridge</li>
    <li>Petermast</li>
  </ul>
  <ul class="list list--specialties-b">
    <li>Corvane</li>
    <li>Alderway</li>
    <li>Izeno</li>
    <li>Havo</li>
    <li>And More</li>
  </ul>

  <div class="regions">
    <span style="left:141px;">LA</span>
    <span style="left:281px;">-</span>
    <span style="left:382px;">OC</span>
    <span style="left:484px;">-</span>
    <span style="left:563px;">IE</span>
  </div>
</section>

</body>
</html>
```